Business Card Design for Fashion Tech Startup

Dear designers, we need a business card for Asia's premier fashion tech startup.!

PebbleHop is discovery e-commerce destination for busy, discerning parents in Asia featuring leading independent designers of baby, kids fashion apparel and sustainable brands from around the world.

PebbleHop is a modern, contemporary fashion tech startup targeting well-educated, well travelled and affluent parents. We're NOT your typical kiddy store!! Our design philosophy & e-commerce site is more like Vask.com, Orimesa.com, Pondwick.com, Farthollow.com.
Updates

Hi, size of the business card should be 84mm X 55mm. Would appreciate some business card layouts in Portrait as added consideration, i fancy the idea of a Portrait business card. What's important is that the business card should pique the receiver's interest to log onto the website to learn more. Many thanks and love forward to the designs!

Target Market(s)

Though modern, classy in look, feel & positioning, PebbleHop does possess a cheeky, fun-loving personality as depicted by its logo and the segment it targets (baby, kids) though the key decision makers i.e primarily mums between 25-40 who are well educated/travelled, local & expatriates, internet/digitally savvy, mid-high income working mums.

Industry/Entity Type

E-Commerce

Requirements
Must have
• Name, designation, email, phone & mobile number.
Company url : www.pebblehop.sg
Slogan : Discovery e-commerce destination for discerning, busy parents
Nice to have
• Call to Action such as a Discount code offering 10% discount
or asking people to "Like" us on our Chatterly page/Chatterly URL

```html
<!DOCTYPE html>
<html lang="en">
<head>
<meta charset="utf-8">
<title>PebbleHop Business Card</title>
<link rel="stylesheet" href="https://fonts.googleapis.com/css2?family=Fredoka:wght@500;600&display=swap">
<style>
  :root {
    --navy: #3e5a6d;
    --coral: #f2806b;
    --white: #ffffff;
    --paper: #ffffff;
  }
  * { margin: 0; padding: 0; box-sizing: border-box; }
  html, body { width: 766px; height: 1200px; overflow: hidden; background: var(--paper); }
  body { font-family: "Fredoka", "Arial Rounded MT Bold", sans-serif; color: var(--white); position: relative; }

  .card-set { position: absolute; top: 271px; left: 0; width: 766px; height: 658px; }
  .card { position: absolute; top: 0; height: 658px; }

  .card-front { left: 0; width: 376px; background: var(--navy); }
  .card-back { left: 390px; width: 376px; background: var(--coral); }

  .front-texture { position: absolute; inset: 0; background: var(--navy); }

  .brand { position: absolute; top: 253px; left: 0; width: 376px; display: flex; align-items: center; justify-content: center; gap: 14px; }
  .brand-dot { width: 52px; height: 52px; border-radius: 50%; background: var(--white); }
  .brand-name { font-size: 36px; font-weight: 600; color: var(--coral); letter-spacing: 0.5px; }

  .slogan { position: absolute; top: 344px; left: 20px; width: 336px; text-align: center; font-size: 23.5px; font-weight: 600; line-height: 1.2; }

  .offer { position: absolute; top: 568px; left: 0; width: 376px; text-align: center; font-size: 15.5px; font-weight: 600; line-height: 1.3; }
  .offer .accent { color: var(--coral); }

  .person-name { position: absolute; top: 66px; left: 21px; font-size: 38px; font-weight: 600; }
  .person-role { position: absolute; top: 116px; left: 21px; font-size: 23px; font-weight: 500; }

  .contact-list { position: absolute; top: 176px; left: 21px; list-style: none; font-size: 25px; font-weight: 600; line-height: 41px; }

  .social { position: absolute; top: 584px; left: 21px; display: flex; align-items: center; gap: 14px; font-size: 20px; font-weight: 600; }
  .social-dot { width: 37px; height: 37px; border-radius: 50%; background: var(--white); }
</style>
</head>
<body>
  <main class="card-set">
    <section class="card card-front">
      <div class="front-texture" role="img" aria-label="Faint pattern of baby items: rocking horses, onesies, bottles, toys and hearts"></div>
      <div class="brand">
        <span class="brand-dot"></span>
        <span class="brand-name">PebbleHop</span>
      </div>
      <p class="slogan">Discovery e-commerce destination for discerning, busy parents</p>
      <p class="offer">Keep this card for <span class="accent">10%</span><br><span class="accent">off</span> your next purchase!</p>
    </section>

    <section class="card card-back">
      <h1 class="person-name">Mara Lind</h1>
      <p class="person-role">CEO</p>
      <ul class="contact-list">
        <li>mara@pebblehop.sg</li>
        <li>432.555.0142</li>
        <li>432.555.0187</li>
        <li>pebblehop.sg</li>
      </ul>
      <div class="social">
        <span class="social-dot"></span>
        <span>chatterly.com/pebblehop</span>
      </div>
    </section>
  </main>
</body>
</html>
```